Wex2Legal Letterhead

Need a new letterhead for my law firm.
IDENTIFYING INFORMATION BELOW:
Teodoro R Galvani III
Attorney at Law
Address: 2834 Brackett Ave, Ste 300, Dallas, TX 75204
Phone: 877-642-7183
Fax: 469-538-2716
Email: ted@wex2legal-example.com
Website: www.wex2legal-example.com

Colors
0054AA
0677BA
7BADD7
CADEEF
E8F1F8

Requirements
Must have
• Logo needs to be on the letterhead, along with identifying information which is included in the project description.

```html
<!DOCTYPE html>
<html lang="en">
<head>
<meta charset="utf-8">
<title>Wex2Legal Letterhead</title>
<link href="https://fonts.googleapis.com/css2?family=Montserrat:wght@300;400;500;800&family=Arimo:wght@400;700&display=swap" rel="stylesheet">
<style>
  :root {
    --backdrop: #b0afb0;
    --paper: #ffffff;
    --navy: #0054aa;
    --blue: #0677ba;
    --sky: #0a9ad8;
    --ink: #111111;
    --text: #8a8a8a;
    --text-dark: #444444;
    --black: #000000;
  }
  * { margin: 0; padding: 0; box-sizing: border-box; }
  html, body { width: 1200px; height: 1200px; overflow: hidden; background: var(--backdrop); }
  .letterhead {
    position: absolute; left: 230px; top: 75px; width: 740px; height: 1045px;
    background: var(--paper); overflow: hidden;
    font-family: "Montserrat", sans-serif;
  }
  .side-band {
    position: absolute; left: 0; top: 0; width: 366px; height: 1045px;
    background: linear-gradient(180deg, var(--navy) 0%, var(--blue) 45%, var(--sky) 100%);
  }
  .sheet {
    position: absolute; left: 16px; top: 0; right: 0; height: 941px;
    background: var(--paper); border-bottom-left-radius: 40px;
  }
  .brand { position: absolute; left: 0; right: 0; top: 52px; text-align: center; }
  .brand-name {
    font-weight: 800; font-size: 36px; letter-spacing: 1px; color: var(--ink); line-height: 40px;
  }
  .brand-tagline {
    font-weight: 400; font-size: 14.5px; letter-spacing: 2.6px; color: var(--ink); margin-top: 2px;
  }
  .recipient { position: absolute; left: 75px; top: 233px; }
  .recipient-label { font-size: 13px; letter-spacing: 2px; color: var(--text-dark); font-weight: 400; }
  .recipient-name { font-size: 13px; color: var(--sky); margin-top: 7px; margin-bottom: 6px; }
  .recipient-line { font-size: 10px; color: var(--text); font-weight: 300; line-height: 16.4px; }
  .letter-date { position: absolute; right: 76px; top: 234px; font-size: 10.5px; color: var(--text-dark); }
  .letter-body {
    position: absolute; left: 75px; top: 373px; width: 590px;
    font-size: 10.8px; line-height: 13.2px; font-weight: 300; color: var(--text); text-align: justify;
  }
  .letter-body p { margin-bottom: 13.2px; }
  .signature { position: absolute; left: 74px; top: 740px; width: 130px; height: 28px;
    background: linear-gradient(90deg, #e9e9e9, #f4f4f4); border-radius: 4px; }
  .signer { position: absolute; left: 74px; top: 777px; }
  .signer-name { font-size: 12.5px; color: var(--text-dark); }
  .signer-title { font-size: 9.5px; color: var(--text); font-weight: 300; margin-top: 2px; }
  .footer-identity {
    position: absolute; left: 0; top: 941px; width: 366px; height: 104px;
    background: linear-gradient(90deg, var(--sky) 0%, var(--blue) 55%, var(--navy) 100%);
    font-family: "Arimo", sans-serif; color: #fff; padding: 22px 0 0 38px;
  }
  .footer-name { font-weight: 700; font-size: 12.8px; line-height: 14.5px; }
  .footer-role, .footer-address { font-size: 12.5px; line-height: 15px; }
  .footer-address { margin-top: 7px; }
  .footer-contact {
    position: absolute; left: 374px; top: 941px; width: 366px; height: 104px;
    background: var(--black); font-family: "Arimo", sans-serif; color: #fff;
    display: flex; justify-content: flex-end; padding: 20px 20px 0 0;
  }
  .contact-list { display: flex; flex-direction: column; }
  .contact-row { display: flex; align-items: center; font-size: 12.5px; line-height: 17.6px; white-space: nowrap; }
  .contact-row svg { width: 10px; height: 10px; margin-right: 4px; fill: var(--sky); flex: none; }
</style>
</head>
<body>
<main class="letterhead">
  <div class="side-band"></div>
  <section class="sheet">
    <header class="brand">
      <div class="brand-name">WEX2LEGAL</div>
      <div class="brand-tagline">COUNSEL YOU CAN TRUST</div>
    </header>

    <div class="recipient">
      <div class="recipient-label">TO</div>
      <div class="recipient-name">Daniel Harrow</div>
      <div class="recipient-line">Human Resources</div>
      <div class="recipient-line">Northfield Inc.</div>
      <div class="recipient-line">2207-B Larkspur Row, Easton</div>
      <div class="recipient-line">E41 USA</div>
    </div>
    <div class="letter-date">Friday, 01/01/2018</div>

    <article class="letter-body">
      <p>Lorem ipsum dolor sit amet, consectetuer adipiscing elit, sed diam nonmmy nibh euismod tincidunt ut laoreet dolore magna aliquam erat volutpat. Ut wisi enim ad minim veniam, quis nostrud exerci tationmcorper suscipit lobortis nisl ut aliquip ex ea commodo consequat. Duis autem vel eum iriure dolor in hendrerit in vulputate velit esse molestie consequat, vel illum dolore eu feugiat nulla facilisis at vero eros et accumsan et iusto odio dignissim qui blandit praesent luptatum zzril delenit augue duis dolore te feugait nulla facilisi.</p>
      <p>Nam liber tempor cum soluta nobis eleifend option congue nihil imprdiet doming id quod mazim placerat facer possim assum. Typi non habent claritatem insitam;</p>
      <p>Est usus legentis in iis qui facit eorum claritatem.</p>
      <p>Investigationes demonstraverunt lectores legere me lius quod ii legunt saepius. Claritas est etiam processus dynamicus, qui sequitur mutationem consuetudium lectorum. Mirum est notare quam littera gothica, quam nunc putamus parum claram, anteposuerit litterarum formas humanitatis per seacula quarta decima et quinta decima. Eodem modo typi, qui nunc nobis videntur parum clari, fiant sollemnes in futurum.</p>
      <p>consectetuer adipiscing elit, sed diam nonummy nibh euismod tincidunt ut laoreet dolore magna aliquam erat volutpat. Ut wisi enim ad minim veniam, quis nostrud exerci tation ullamcorper suscipit lobortis nisl ut aliquip ex ea commodo consequat. Duis autem vel eum iriure dolor in hendrerit in vulputate velit esse molestie consequat, vel illum dolore eu feugiat nulla facilisis at vero eros et accumsan et iusto odio dignissim qui blandit praesent luptatum zzril delenit augue duis dolore te feugait nulla facilisi.</p>
      <p>Nam liber tempor cum soluta nobis eleifend option congue nihil imperdiet .</p>
    </article>

    <div class="signature" role="img" aria-label="Handwritten signature of Peter Lindqvist"></div>
    <div class="signer">
      <div class="signer-name">Peter Lindqvist</div>
      <div class="signer-title">Managing Director</div>
    </div>
  </section>

  <footer class="footer-identity">
    <div class="footer-name">Teodoro R Galvani III</div>
    <div class="footer-role">Attorney at Law</div>
    <div class="footer-address">2834 Brackett Ave<br>Ste 300, Dallas, TX 75204</div>
  </footer>
  <footer class="footer-contact">
    <div class="contact-list">
      <div class="contact-row">
        <svg viewBox="0 0 10 10" aria-hidden="true"><path d="M2 0.5l1.8 2.2-1 1.2c.6 1.3 1.5 2.2 2.8 2.8l1.2-1 2.2 1.8-1 2c-4 .2-7.7-3.5-7.5-7.5z"/></svg>877-642-7183
      </div>
      <div class="contact-row">
        <svg viewBox="0 0 10 10" aria-hidden="true"><path d="M2.5 0h5v3h-5zM0 3.5h10v4.5H8V6H2v2H0zM2.5 6.8h5V10h-5z"/></svg>469-538-2716
      </div>
      <div class="contact-row">
        <svg viewBox="0 0 10 10" aria-hidden="true"><path d="M0 2h10v6H0zM.6 2.4L5 5.8l4.4-3.4" stroke="#000" stroke-width=".7"/></svg>ted@wex2legal-example.com
      </div>
      <div class="contact-row">
        <svg viewBox="0 0 10 10" aria-hidden="true"><circle cx="5" cy="5" r="4.6"/><path d="M.5 5h9M5 .5c-2.4 2.6-2.4 6.4 0 9M5 .5c2.4 2.6 2.4 6.4 0 9" stroke="#000" stroke-width=".7" fill="none"/></svg>www.wex2legal-example.com
      </div>
    </div>
  </footer>
</main>
</body>
</html>
```